New Business Card Design Project

Hi! I would like for you to design a business card for our aesthetic injections business. We offer Zelvia, filler, skin care. I would like it to be elegant, feminine, modern and sleek/clean. I like black/gold foil/ivory/parchment colors. It can be either one or two sided. I would like matte black with gold foil logo on one side and ivory with gold foil information on the other side

Target Market(s)

target market is the discerning woman who wants to look her best

Industry/Entity Type

beauty

Contact Information for Business Card

logo, name, phone, email, website, instagram, facebook, location

Requirements
Must have
• logo and info
Nice to have
• the icons for cell, instagram, email, fb etc
Should not have
• images of people

```html
<!DOCTYPE html>
<html lang="en">
<head>
<meta charset="utf-8">
<title>Velora Skin Studio – Business Card</title>
<link rel="stylesheet" href="https://fonts.googleapis.com/css2?family=Roboto:wght@400;500;700&display=swap">
<style>
  :root {
    --backdrop: #dddbd7;
    --card-black: #1f1f1f;
    --gold: #d9b95a;
    --gold-soft: #c8a84c;
    --card-edge: #b89a3e;
  }
  * { margin: 0; padding: 0; box-sizing: border-box; }
  html, body {
    width: 1200px;
    height: 817px;
    overflow: hidden;
    background: var(--backdrop);
    font-family: "Roboto", Arial, sans-serif;
  }
  .canvas {
    position: relative;
    width: 1200px;
    height: 817px;
  }
  .card {
    position: absolute;
    top: 265px;
    width: 500px;
    height: 286px;
    background: var(--card-black);
    border-bottom: 3px solid var(--card-edge);
    color: var(--gold);
  }
  .card--front { left: 70px; }
  .card--back { left: 630px; }

  .brand {
    display: flex;
    align-items: center;
    gap: 10px;
    font-weight: 500;
    color: var(--gold);
    letter-spacing: 0.04em;
  }
  .brand__dot {
    width: 10px;
    height: 10px;
    border-radius: 50%;
    background: var(--gold);
    flex: none;
  }
  .card--front .brand {
    position: absolute;
    left: 50%;
    top: 105px;
    transform: translateX(-50%);
    font-size: 26px;
    white-space: nowrap;
  }
  .socials {
    position: absolute;
    left: 0;
    right: 0;
    bottom: 30px;
    display: flex;
    justify-content: center;
    gap: 22px;
    font-size: 12px;
    color: var(--gold);
  }
  .socials__item { display: flex; align-items: center; gap: 6px; }
  .socials__mark {
    width: 10px;
    height: 10px;
    background: var(--gold);
    border-radius: 2px;
  }

  .card--back .brand {
    position: absolute;
    left: 40px;
    top: 132px;
    font-size: 19px;
    white-space: nowrap;
  }
  .divider {
    position: absolute;
    left: 258px;
    top: 60px;
    width: 1px;
    height: 166px;
    background: var(--gold-soft);
  }
  .contact {
    position: absolute;
    left: 280px;
    top: 62px;
    font-size: 12px;
    line-height: 1.45;
  }
  .contact__name {
    font-size: 17px;
    font-weight: 700;
    letter-spacing: 0.02em;
  }
  .contact__role { margin-bottom: 20px; }
  .contact__address { margin-bottom: 8px; }
  .contact__line { display: flex; align-items: center; gap: 6px; }
  .contact__line svg { width: 11px; height: 11px; flex: none; }
</style>
</head>
<body>
<main class="canvas">
  <section class="card card--front" aria-label="Card front">
    <div class="brand"><span class="brand__dot"></span>Velora Skin Studio</div>
    <div class="socials">
      <span class="socials__item"><span class="socials__mark"></span>@veloraskinstudio</span>
      <span class="socials__item"><span class="socials__mark"></span>@veloraskinstudio</span>
    </div>
  </section>

  <section class="card card--back" aria-label="Card back">
    <div class="brand"><span class="brand__dot"></span>Velora Skin Studio</div>
    <div class="divider"></div>
    <div class="contact">
      <p class="contact__name">DANA WHITFIELD</p>
      <p class="contact__role">Operations Manager</p>
      <p class="contact__address">48 Maple Crest Road,<br>Oakridge, ON L2K 5T1</p>
      <p class="contact__line">
        <svg viewBox="0 0 12 12" aria-hidden="true"><path d="M3 1 L5 3.5 L4 5 Q5.5 7 7 8 L8.5 7 L11 9 L9.5 11 Q4 10 1 2.5 Z" fill="var(--gold)"/></svg>
        905-555-0147
      </p>
      <p class="contact__line">
        <svg viewBox="0 0 12 12" aria-hidden="true"><rect x="1" y="2.5" width="10" height="7" fill="none" stroke="var(--gold)" stroke-width="1.2"/><path d="M1 2.5 L6 6.5 L11 2.5" fill="none" stroke="var(--gold)" stroke-width="1.2"/></svg>
        info@veloraskin.ca
      </p>
      <p class="contact__line">
        <svg viewBox="0 0 12 12" aria-hidden="true"><circle cx="6" cy="6" r="5" fill="none" stroke="var(--gold)" stroke-width="1.1"/><ellipse cx="6" cy="6" rx="2.2" ry="5" fill="none" stroke="var(--gold)" stroke-width="1"/><path d="M1 6 H11" stroke="var(--gold)" stroke-width="1"/></svg>
        www.veloraskin.ca
      </p>
    </div>
  </section>
</main>
</body>
</html>
```